Ridgeline Trek Supply - Business Card Design Project

Our company is Ridgeline Trek Supply. We make outdoor gear such as headlamps and flashlights. If you would like to get a feel for our company, feel free to look at our website. www.ridgelinetreksupply.example

And here is my information to put on the card.
Ridgeline Trek Supply
Delia Fenwick
41963 Willowbend Hollow Road
Bandon, OR. 97520
support@RidgelineTrekSupply.example
www.RidgelineTrekSupply.example
Facebook.com/RidgelineTrekSupply
Pinterest.com/RidgelineTrekSupply
Twitter.com/RidgelineTrekSupply

Target Market(s)

hunters, campers, preppers

Industry/Entity Type

Sporting Good

Contact Information for Business Card

We would like a card that looks a little outdoorsy. We have 2 logos so one of them should be on the card. The card should also use the colors that are on our logos. The name "Ridgeline Trek Supply" if written out should be in the font "Capture it".

Requirements
Must have
• We currently have 2 logos. At least one must be on the card.
• Must use colors from the logos.
Nice to have
• Possibly a quote from our website. Something like: We don’t just make outdoor gear. We use it. We know it. We live it and we love it.

```html
<!DOCTYPE html>
<html lang="en">
<head>
<meta charset="utf-8">
<title>Ridgeline Trek Supply – Business Card</title>
<link rel="stylesheet" href="https://fonts.googleapis.com/css2?family=Open+Sans:wght@400;700&display=swap">
<style>
  :root {
    --backdrop: #3b3b3b;
    --card-white: #ffffff;
    --bark-brown: #43301b;
    --trail-gold: #b8955a;
    --ink: #111111;
    --brand-brown: #4a3520;
  }
  * { margin: 0; padding: 0; box-sizing: border-box; }
  html, body {
    width: 999px; height: 1200px; overflow: hidden;
    background: var(--backdrop);
    font-family: "Open Sans", Arial, sans-serif;
  }
  .canvas { position: relative; width: 999px; height: 1200px; }

  .card {
    position: absolute; left: 45px; width: 908px; height: 518px;
    overflow: hidden;
  }
  .card-front { top: 62px; background: var(--card-white); }
  .card-back { top: 609px; background: var(--bark-brown); }

  .brand {
    position: absolute; left: 0; right: 0;
    display: flex; align-items: center; justify-content: center; gap: 16px;
    font-weight: 700;
  }
  .brand-dot { border-radius: 50%; background: var(--trail-gold); flex: none; }
  .card-front .brand { top: 150px; color: var(--brand-brown); font-size: 40px; }
  .card-front .brand-dot { width: 34px; height: 34px; }
  .card-back .brand { top: 220px; color: #ffffff; font-size: 52px; }
  .card-back .brand-dot { width: 44px; height: 44px; }

  .holder { position: absolute; left: 45px; top: 288px; color: var(--ink); }
  .holder-name { font-size: 30px; font-weight: 700; line-height: 1; letter-spacing: 0.2px; }
  .holder-role { font-size: 21px; margin-top: 14px; margin-left: 2px; }
  .holder-address { font-size: 21px; line-height: 30px; margin-top: 18px; margin-left: 2px; }

  .contacts {
    position: absolute; left: 488px; top: 266px; list-style: none;
    font-size: 18.5px; color: var(--ink);
  }
  .contacts li { display: flex; align-items: center; height: 30.2px; }
  .contacts .icon { width: 22px; height: 22px; margin-right: 23px; flex: none; }
  .contacts .icon-square { width: 18px; height: 18px; margin: 0 25px 0 2px; background: var(--ink); border-radius: 2px; }

  .band { position: absolute; left: 0; bottom: 0; width: 908px; height: 90px; }
</style>
</head>
<body>
<div class="canvas">

  <section class="card card-front">
    <div class="brand"><span class="brand-dot"></span><span class="brand-name">Ridgeline Trek Supply</span></div>

    <div class="holder">
      <p class="holder-name">Delia Fenwick</p>
      <p class="holder-role">Designation</p>
      <p class="holder-address">41963 Willowbend Hollow Road<br>Bandon, OR. 97520</p>
    </div>

    <ul class="contacts">
      <li>
        <svg class="icon" viewBox="0 0 22 22"><path d="M2 9 L11 3 L20 9 V19 H2 Z" fill="#111"/><path d="M4 10 L11 15 L18 10" fill="none" stroke="#fff" stroke-width="1.6"/></svg>
        support@RidgelineTrekSupply.example
      </li>
      <li>
        <svg class="icon" viewBox="0 0 22 22" fill="none" stroke="#111" stroke-width="1.3"><circle cx="11" cy="11" r="8.5"/><ellipse cx="11" cy="11" rx="3.8" ry="8.5"/><path d="M2.5 11 H19.5 M4 6.5 H18 M4 15.5 H18"/></svg>
        www.RidgelineTrekSupply.example
      </li>
      <li><span class="icon-square"></span>/RidgelineTrekSupply</li>
      <li><span class="icon-square"></span>/RidgelineTrekSupply</li>
      <li><span class="icon-square"></span>/RidgelineTrekSupply</li>
    </ul>

    <svg class="band" viewBox="0 0 908 90" preserveAspectRatio="none">
      <path d="M0 23 H470 C515 23 520 0 568 0 H908 V90 H0 Z" fill="var(--trail-gold)"/>
      <path d="M0 48 H470 C530 48 520 0 568 0 H908 V90 H0 Z" fill="var(--bark-brown)"/>
    </svg>
  </section>

  <section class="card card-back">
    <div class="brand"><span class="brand-dot"></span><span class="brand-name">Ridgeline Trek Supply</span></div>
  </section>

</div>
</body>
</html>
```